Conversion Optimisation Checklist for eCommerce websites

We need a design for a 2 page pdf checklist (attached document outline), the first page is checklist. Document will be primarly for digital viewing - don't need to worry about print. Should have our website address (torvo.com.au), email (hello@torvo.com.au) and phone number (1300 482 917) in the footer
The second page is a bonus, a wireframe of an ecommerce homepage with annotations to show what information is important where.
Should be branded with our branding (logo attached) and compliment the design (colours/style/imagery) of an accompanying landing page design (attached).

We are a website and marketing agency thank helps young ecommerce businesses to grow faster.

```html
<!DOCTYPE html>
<html lang="en">
<head>
<meta charset="utf-8">
<title>Torvo – Lead Magnet Checklist</title>
<link href="https://fonts.googleapis.com/css2?family=Montserrat:wght@400;500;700;800&family=Permanent+Marker&display=swap" rel="stylesheet">
<style>
:root{
  --navy:#0f1e31;
  --navy-2:#2b4a5d;
  --blue:#2b8fd6;
  --blue-light:#3a9be0;
  --ink:#1b2b3e;
  --text:#4a5560;
  --muted:#8a939b;
  --paper:#ffffff;
  --panel:#eef0f2;
  --wire:#e4e6e8;
  --wire-fill:#f3f4f5;
  --stage:#6b6b6b;
}
*{box-sizing:border-box;margin:0;padding:0}
html,body{width:1200px;height:888px;overflow:hidden}
body{background:var(--stage);font-family:"Montserrat",sans-serif;position:relative}
.page{position:absolute;top:86px;width:506px;height:716px;background:var(--paper);overflow:hidden}
.page--checklist{left:67px}
.page--wireframe{left:626px}
.header{position:absolute;left:0;top:0;width:100%;height:200px;background:linear-gradient(100deg,var(--navy) 40%,var(--navy-2))}
.brush{position:absolute;left:0;top:172px;width:506px;height:50px}
.logo{position:absolute;left:36px;top:36px;display:flex;align-items:center;gap:7px;color:#fff;font-weight:800;font-size:20px;letter-spacing:1px}
.logo__mark{width:22px;height:22px;border-radius:50%;background:var(--blue)}
.title{position:absolute;left:40px;top:94px;color:#fff;font-family:"Permanent Marker",cursive;font-size:38px;font-weight:400;letter-spacing:1px;line-height:44px}
.subtitle{position:absolute;left:41px;top:149px;color:#fff;font-size:11px;line-height:13px}
.subtitle b{color:var(--blue-light)}
.device{position:absolute;left:349px;top:66px;width:157px;height:140px;background:linear-gradient(160deg,#f4f5f6,#d9dcdf);border-radius:4px 0 0 4px;z-index:2}
.section{position:absolute}
.section--left{width:176px}
.section--right{width:212px}
.section__head{display:flex;align-items:center;gap:4px;font-size:13px;font-weight:800;color:var(--ink);margin-bottom:9px;line-height:16px}
.section__head span{color:var(--blue)}
.section__head::before{content:"";order:3;width:4px;height:4px;border-radius:50%;background:var(--blue);margin-left:8px}
.section__head::after{content:"";order:4;flex:1;height:1px;background:var(--blue)}
.item{display:flex;gap:9px;align-items:flex-start;height:27px;font-size:8.6px;line-height:10.4px;color:var(--text)}
.tick{flex:none;width:14px;height:14px;border:1px solid var(--blue);border-radius:50%;position:relative;margin-top:1px}
.tick::after{content:"";position:absolute;left:3px;top:4px;width:4px;height:4px;border-top:1.3px solid var(--blue);border-right:1.3px solid var(--blue);transform:rotate(45deg)}
.engage{position:absolute;left:0;top:602px;width:506px;height:114px;background:var(--panel)}
.engage__brush{position:absolute;left:0;top:582px;width:506px;height:22px}
.engage__title{position:absolute;left:42px;top:18px;font-size:13px;font-weight:800;line-height:15px;color:var(--ink)}
.engage__title span{color:var(--blue)}
.engage .item{position:absolute;width:150px}
/* wireframe page */
.label{position:absolute;font-size:6.6px;line-height:8px;color:var(--muted)}
.label--left{right:400px;text-align:right;white-space:nowrap}
.label--side{left:397px;white-space:nowrap}
.dot{position:absolute;width:8px;height:8px;border:1px solid #c7ccd0;border-radius:50%}
.dot--l{left:112px}
.dot--r{left:383px}
.wire{position:absolute;left:126px;top:273px;width:247px;height:366px;background:var(--wire-fill)}
.block{position:absolute;background:var(--wire)}
.box{position:absolute;background:var(--wire-fill);border:1px solid #8fc0e6;border-radius:1px}
.btn{position:absolute;height:9px;background:var(--blue);border-radius:1px}
.btn--ghost{background:transparent;border:1px solid var(--blue)}
.footer-brush{position:absolute;left:0;top:652px;width:506px;height:24px}
.footer{position:absolute;left:0;top:691px;width:100%;height:14px;font-size:8.5px;font-weight:700;color:var(--blue)}
.footer__item{position:absolute;top:0;display:flex;align-items:center;gap:5px;height:14px}
.footer .logo{position:static;color:var(--ink);font-size:13px;gap:5px}
.footer .logo__mark{width:13px;height:13px}
</style>
</head>
<body>

<!-- Page 1: checklist -->
<section class="page page--checklist">
  <div class="header"></div>
  <svg class="brush" viewBox="0 0 506 50" preserveAspectRatio="none">
    <path d="M0,16 L180,12 L360,6 L506,0 L506,22 L360,28 L180,36 L0,44 Z" fill="#2b8fd6"/>
    <path d="M0,44 L180,36 L360,28 L506,22 L506,50 L0,50 Z" fill="#fff"/>
  </svg>
  <div class="logo"><span class="logo__mark"></span>TORVO</div>
  <h1 class="title">Lead Magnet</h1>
  <p class="subtitle"><b>25-Step</b> Checklist to Optimise your<br>Website and Increase Sales Conversions</p>
  <div class="device" role="img" aria-label="Laptop and phone showing an ecommerce store"></div>

  <div class="section section--left" style="left:39px;top:254px">
    <h2 class="section__head"><span>BE</span>COMPELLING</h2>
    <div class="item"><i class="tick"></i>Encourage purchases with featured products or sales</div>
    <div class="item"><i class="tick"></i>Draw attention to popular<br>(or profitable) products</div>
    <div class="item"><i class="tick"></i>Clearly show discounted pricing<br>and the benefit</div>
    <div class="item"><i class="tick"></i>Encourage purchases over a free<br>shipping threshold</div>
    <div class="item"><i class="tick"></i>Make your site messaging reflect the key benefits your products provide</div>
  </div>
  <div class="section section--right" style="left:255px;top:254px">
    <h2 class="section__head"><span>BUILD</span>TRUST</h2>
    <div class="item" style="height:37px"><i class="tick"></i>Includes your phone number on key areas people might have questions like the cart or checkout</div>
    <div class="item"><i class="tick"></i>Ensure your site uses a SSL certificate<br>and loads over https</div>
    <div class="item" style="height:17px"><i class="tick"></i>Offer different payment methods</div>
    <div class="item"><i class="tick"></i>Have a professional<br>design</div>
    <div class="item"><i class="tick"></i>Have all the information customers need including shipping, returns &amp; delivery policies</div>
  </div>
  <div class="section section--left" style="left:39px;top:426px">
    <h2 class="section__head"><span>BE</span>SIMPLE</h2>
    <div class="item"><i class="tick"></i>Make navigation<br>clear &amp; simple</div>
    <div class="item"><i class="tick"></i>Display products and their<br>price clearly</div>
    <div class="item"><i class="tick"></i>Have additional information for<br>products that need it</div>
    <div class="item"><i class="tick"></i>Use high quality images to show<br>off your product</div>
    <div class="item"><i class="tick"></i>Ensure you have appropriate shipping methods setup for your customers</div>
  </div>
  <div class="section section--right" style="left:255px;top:426px">
    <h2 class="section__head"><span>DRIVE</span>TRAFFIC</h2>
    <div class="item"><i class="tick"></i>Ensure your website is setup and<br>optimised for search keywords</div>
    <div class="item"><i class="tick"></i>Ensure reporting &amp; tracking<br>is in place</div>
    <div class="item"><i class="tick"></i>Consider paid marketing and measure<br>your ROI through analytics</div>
    <div class="item"><i class="tick"></i>Regularly review<br>reports</div>
    <div class="item"><i class="tick"></i>Build interesting and insightful content<br>around your products</div>
  </div>

  <svg class="engage__brush" viewBox="0 0 506 22" preserveAspectRatio="none">
    <path d="M0,20 L200,18 L330,14 L420,8 L506,4 L506,22 L0,22 Z" fill="#eef0f2"/>
    <path d="M330,14 L420,6 L506,0 L506,10 L420,14 L330,17 Z" fill="#2b8fd6"/>
  </svg>
  <div class="engage">
    <h2 class="engage__title"><span>ENGAGE YOUR</span><br>CUSTOMERS</h2>
    <div class="item" style="left:182px;top:20px;width:160px"><i class="tick"></i>Email customers that abandon<br>their cart before purchasing</div>
    <div class="item" style="left:346px;top:20px;width:130px"><i class="tick"></i>Reward loyal &amp; repeat<br>customers</div>
    <div class="item" style="left:40px;top:56px;width:135px;height:34px"><i class="tick"></i>Engage with customers<br>on social media through<br>related groups or pages</div>
    <div class="item" style="left:182px;top:56px;width:160px;height:34px"><i class="tick"></i>Use email automation to<br>follow up existing customers<br>with offers or promotions</div>
    <div class="item" style="left:346px;top:56px;width:130px"><i class="tick"></i>Setup a referral bonus<br>for new customers</div>
  </div>
</section>

<!-- Page 2: wireframe -->
<section class="page page--wireframe">
  <div class="header"></div>
  <svg class="brush" viewBox="0 0 506 50" preserveAspectRatio="none">
    <path d="M0,16 L180,12 L360,6 L506,0 L506,22 L360,28 L180,36 L0,44 Z" fill="#2b8fd6"/>
    <path d="M0,44 L180,36 L360,28 L506,22 L506,50 L0,50 Z" fill="#fff"/>
  </svg>
  <div class="logo"><span class="logo__mark"></span>TORVO</div>
  <h1 class="title">Lead Magnet</h1>
  <p class="subtitle"><b>25-Step</b> Checklist to Optimise your<br>Website and Increase Sales Conversions</p>
  <div class="device" role="img" aria-label="Laptop and phone showing an ecommerce store"></div>

  <p class="label" style="left:128px;top:240px">Home Page</p>
  <p class="label" style="left:235px;top:240px">Search bar</p>
  <p class="label" style="left:330px;top:237px">Currency display if multicurrency or<br>unclear to all traffic sources</p>
  <i class="dot" style="left:144px;top:257px"></i>
  <i class="dot" style="left:250px;top:257px"></i>
  <i class="dot" style="left:348px;top:257px"></i>

  <div class="wire">
    <div class="block" style="left:5px;top:13px;width:32px;height:14px"></div>
    <div class="block" style="left:95px;top:13px;width:57px;height:14px"></div>
    <div class="block" style="left:202px;top:13px;width:39px;height:14px"></div>
    <div class="block" style="left:5px;top:31px;width:236px;height:10px"></div>
    <div class="block" style="left:5px;top:45px;width:236px;height:66px"></div>
    <div class="btn" style="left:13px;top:56px;width:84px"></div>
    <div class="btn" style="left:13px;top:69px;width:84px"></div>
    <div class="btn btn--ghost" style="left:13px;top:83px;width:32px"></div>
    <div class="block" style="left:5px;top:111px;width:236px;height:11px"></div>
    <div class="box" style="left:5px;top:133px;width:69px;height:32px"></div>
    <div class="box" style="left:88px;top:133px;width:69px;height:32px"></div>
    <div class="box" style="left:171px;top:133px;width:70px;height:32px"></div>
    <div class="box" style="left:5px;top:175px;width:56px;height:36px"></div>
    <div class="box" style="left:5px;top:221px;width:56px;height:36px"></div>
    <div class="box" style="left:188px;top:175px;width:53px;height:36px"></div>
    <div class="box" style="left:188px;top:221px;width:53px;height:36px"></div>
    <div class="box" style="left:61px;top:175px;width:127px;height:82px"></div>
    <div class="box" style="left:5px;top:272px;width:56px;height:36px"></div>
    <div class="box" style="left:65px;top:272px;width:56px;height:36px"></div>
    <div class="box" style="left:125px;top:272px;width:56px;height:36px"></div>
    <div class="box" style="left:185px;top:272px;width:56px;height:36px"></div>
    <div class="block" style="left:5px;top:320px;width:236px;height:21px"></div>
    <div class="block" style="left:5px;top:348px;width:52px;height:9px;background:#d9dcdf"></div>
  </div>

  <p class="label label--left" style="top:288px">Logo</p>
  <p class="label label--left" style="top:302px">Simple Navigation<br>with cart</p>
  <p class="label label--left" style="top:378px">Additional messaging<br>around returns or<br>special requirements</p>
  <p class="label label--left" style="top:482px">Exit intent popup<br>with offer</p>
  <p class="label label--left" style="top:544px">Information about your<br>business, why you exist<br>and why your customers<br>should care ideally with<br>a video</p>
  <p class="label label--left" style="top:620px">Site purchase<br>activity dialog</p>
  <i class="dot dot--l" style="top:288px"></i>
  <i class="dot dot--l" style="top:305px"></i>
  <i class="dot dot--l" style="top:386px"></i>
  <i class="dot dot--l" style="top:486px"></i>
  <i class="dot dot--l" style="top:560px"></i>
  <i class="dot dot--l" style="top:624px"></i>

  <p class="label label--side" style="top:271px">Promotional<br>message bar</p>
  <p class="label label--side" style="top:294px">Unique message<br>potentially free ship-<br>ping or other USP of<br>your business</p>
  <p class="label label--side" style="top:344px">Key image with<br>messaging Outlining<br>more benefits of your<br>products<br>And call to action</p>
  <p class="label label--side" style="top:399px">Core Product<br>categories</p>
  <p class="label label--side" style="top:463px">Testimonial</p>
  <p class="label label--side" style="top:507px">Promotional product<br>or categories</p>
  <p class="label label--side" style="top:547px">Top selling products or<br>lastest to be reviewed<br>Showing star ratings<br>and price</p>
  <p class="label label--side" style="top:584px">Newsletter subscription<br>with offer if subscribed</p>
  <p class="label label--side" style="top:606px">Footer with customer care<br>information including<br>return &amp; delivery policy<br>Trust symbols like accepted<br>credit cards and/or SSL<br>secure badges</p>
  <i class="dot dot--r" style="top:274px"></i>
  <i class="dot dot--r" style="top:296px"></i>
  <i class="dot dot--r" style="top:345px"></i>
  <i class="dot dot--r" style="top:402px"></i>
  <i class="dot dot--r" style="top:462px"></i>
  <i class="dot dot--r" style="top:508px"></i>
  <i class="dot dot--r" style="top:549px"></i>
  <i class="dot dot--r" style="top:584px"></i>
  <i class="dot dot--r" style="top:608px"></i>

  <svg class="footer-brush" viewBox="0 0 506 24" preserveAspectRatio="none">
    <path d="M0,24 L150,21 L300,17 L420,10 L506,4 L506,14 L420,18 L300,22 L150,24 Z" fill="#2b8fd6"/>
  </svg>
  <div class="footer">
    <span class="footer__item" style="left:30px">
      <svg width="9" height="7" viewBox="0 0 9 7"><rect x=".5" y=".5" width="8" height="6" fill="none" stroke="#8a939b"/><path d="M.5,.5 L4.5,4 L8.5,.5" fill="none" stroke="#8a939b"/></svg>hello@torvo.com.au</span>
    <span class="footer__item" style="left:159px">
      <svg width="10" height="10" viewBox="0 0 10 10"><circle cx="5" cy="5" r="4.5" fill="none" stroke="#8a939b"/><path d="M3.3,3 L4.2,2.8 L4.6,4 L4,4.4 Q4.6,5.6 5.6,6 L6,5.4 L7.2,5.8 L7,6.7 Q4,7 3.3,3Z" fill="#8a939b"/></svg>1300 482 917</span>
    <span class="footer__item" style="left:271px">
      <svg width="10" height="10" viewBox="0 0 10 10"><circle cx="5" cy="5" r="4.5" fill="none" stroke="#8a939b"/><ellipse cx="5" cy="5" rx="2" ry="4.5" fill="none" stroke="#8a939b"/><path d="M.5,5 H9.5" stroke="#8a939b"/></svg>torvo.com.au</span>
    <span class="footer__item" style="left:390px"><span class="logo"><span class="logo__mark"></span>TORVO</span></span>
  </div>
</section>

</body>
</html>
```